Wordpress Web Design & Coding for velnoragroup.ca

We need a website for a new investment company that is visually grabbing and vibrant. We would like to see a web page that displays trust, growth and confidence. Needs to be responsive and mobile friendly for all browsers and coded for both Android & IOS.

Open to the number of pages and menu items. I selected 4 but if you feel the layout would work better with less I am open to this. Need to sell the people (management team/related businesses) and then show where the invested money will be going (upcoming projects).

Company Info:

Velnora is an investment company put together by a group of seasoned business professionals who have come together to combine decades of success in the real estate development, management, financing and medical services. The company will be a full service company offering turn key solutions for medical professionals.

Vel-Nora will focus on providing a full range of services via a group of distinct companies to deliver newly emerging needs of the medical community. The end goal will be to create complete solutions for individuals in the medical community. Our group has experience and success with the conceptualization, construction and financing of medical and dental clinic spaces. Vel-Nora Group will be established to accommodate all areas of the development and creation of clinics for medical professionals from building construction to equipment financing and administrations.

You can mention these companies and take photos from their websites. You can also use stock photos.

Our construction partner:
https://382bld.com/projects/

Our equipment leasing partner:
https://www.pordiva.com/

Our Management Team and medical partners

Gil Parkes
https://www.mysoundpoise.ca/

Milos Vendraker
https://www.qrtdentalservices.com/about-us

PROPOSED PROJECTS (see attachment for details)
Hollowmere Business Park
Cresfield Business Park
Mt. Corwin Ridge Professional

Investors

Investment

Sans Serif

Must have
• Wordpress – must be both desktop and mobile friendly with fast page load speed
Ability to edit after ourselves in Wordpress
Attractive home page with logo etc.
Logo colours are: for the blue the pantone color is #0355a3
and for the green is #8cc63f

Sections, about us, what we do/services we provide, contact us

```html
<!DOCTYPE html>
<html lang="en">
<head>
<meta charset="utf-8">
<title>Vel-Nora Group</title>
<link href="https://fonts.googleapis.com/css2?family=Poppins:wght@300;400;500;600&display=swap" rel="stylesheet">
<style>
:root{
  --blue:#0355a3;
  --blue-deep:#0a3f86;
  --green:#8cc63f;
  --green-btn:#6fae3c;
  --ink:#111;
  --text:#6b6b6b;
  --faint:#f1f1f1;
  --dot:#d5d5d5;
  --footer:#0b0b0b;
}
*{margin:0;padding:0;box-sizing:border-box}
html,body{width:1200px;height:3748px;overflow:hidden}
body{font-family:'Poppins',sans-serif;color:var(--ink);background:#fff;position:relative}
.abs{position:absolute}
a{text-decoration:none;color:inherit}

/* brand */
.brand{display:flex;align-items:center;gap:8px;font-weight:600;color:var(--blue);letter-spacing:.5px}
.brand .mark{width:14px;height:14px;background:var(--green)}

/* hero */
.hero{top:0;left:0;width:1200px;height:608px}
.hero-bg{position:absolute;inset:0;background:
  radial-gradient(ellipse at 55% 20%,rgba(120,160,200,.55),transparent 60%),
  linear-gradient(180deg,#3b5577 0%,#4b5b6b 40%,#6b5a4c 70%,#2b2f38 100%)}
.hero .brand{position:absolute;left:113px;top:38px;font-size:20px;color:#fff}
.nav{position:absolute;top:38px;left:0;width:100%;font-size:15px;color:#fff}
.nav a{position:absolute}
.nav .active{color:var(--green)}
.btn-login{position:absolute;left:870px;top:31px;width:96px;height:36px;border:2px solid #fff;border-radius:18px;color:#fff;font-size:15px;display:flex;align-items:center;justify-content:center}
.btn-register{position:absolute;left:979px;top:31px;width:108px;height:36px;background:var(--blue);border-radius:18px;color:#fff;font-size:15px;display:flex;align-items:center;justify-content:center;font-weight:500}
.hero h1{position:absolute;top:255px;width:100%;text-align:center;color:#fff;font-size:44px;font-weight:600;letter-spacing:-.5px}
.hero .lead{position:absolute;top:306px;width:100%;text-align:center;color:#fff;font-size:16px}
.scroll{position:absolute;left:589px;top:552px}

/* section index */
.idx{position:absolute;left:40px}
.idx .num{font-size:26px;font-weight:500;color:var(--blue);line-height:1}
.idx .dots{margin-top:12px;display:flex;flex-direction:column;gap:8px}
.idx .dot{width:8px;height:8px;border-radius:50%;background:var(--dot);position:relative}
.idx .dot.on{background:var(--green)}
.idx .dot span{position:absolute;left:18px;top:-5px;font-size:11px;color:var(--blue);font-weight:500;white-space:nowrap}
.hero .idx .num{color:#fff}
.hero .idx .dot span{color:#fff}
.hero .idx .dot{background:rgba(255,255,255,.5)}
.hero .idx .dot.on{background:var(--green)}

/* headings */
.ghost{position:absolute;font-weight:600;color:var(--faint);line-height:1;white-space:nowrap}
.sec-title{position:absolute;width:1200px;left:0;text-align:center;font-size:35px;font-weight:600;letter-spacing:-.5px}
.sec-sub{position:absolute;width:1200px;left:0;text-align:center;font-size:14px;color:#555}

/* about */
.about-title{left:109px;top:720px;font-size:35px;font-weight:600}
.about-sub{left:110px;top:768px;font-size:14px;color:#555}
.about-rule{left:110px;top:840px;width:53px;height:3px;background:var(--green)}
.about-text{left:601px;top:720px;width:490px;font-size:14px;line-height:28.3px;color:#555}
.learn{left:601px;top:883px;width:164px;height:44px;border:1.5px solid var(--blue);border-radius:22px;display:flex;align-items:center;color:var(--blue);font-weight:500;font-size:16px}
.learn .t{width:118px;text-align:center;border-right:1.5px solid var(--blue);height:100%;display:flex;align-items:center;justify-content:center}
.learn .i{flex:1;display:flex;justify-content:center}
.video{left:112px;top:969px;width:976px;height:384px;background:
  radial-gradient(ellipse at 30% 55%,rgba(120,160,70,.75),transparent 55%),
  linear-gradient(90deg,#8fa56c 0%,#c9d4b8 45%,#eef0f3 70%,#e6e7f0 100%)}
.play{position:absolute;left:556px;top:1114px}

/* services */
.card{position:absolute;top:1596px;width:232px;height:295px;color:#fff;text-align:center;overflow:hidden}
.card .bg{position:absolute;inset:0}
.card .shade{position:absolute;inset:0;background:rgba(10,30,60,.45)}
.card svg{position:absolute;left:89px;top:50px}
.card h3{position:absolute;top:125px;width:100%;font-size:18px;font-weight:500;line-height:25px}
.card .more{position:absolute;left:50%;transform:translateX(-50%);top:203px;width:128px;height:37px;border:1.5px solid #fff;border-radius:19px;font-size:15px;display:flex;align-items:center;justify-content:center}

/* partners */
.partner{position:absolute;top:2131px;width:233px;height:95px;border:2px solid #d7d7d7;background:#fff;display:flex;align-items:center;justify-content:center}
.partner.sel{border:3px solid var(--green)}
.partner.dark{background:#000;border-color:#cfcfcf}
.partner .badge{width:130px;height:26px;background:#c8ccd4;border-radius:3px}
.pointer{position:absolute;left:221px;top:2226px}
.partner-head{left:113px;top:2256px;font-size:18px;font-weight:500;color:#222}
.partner-text{left:113px;top:2288px;width:900px;font-size:13.5px;line-height:27px;color:#777}

/* projects */
.proj-img{position:absolute;top:2577px;height:194px}
.proj{position:absolute;top:2784px;width:313px}
.proj h4{font-size:17.5px;font-weight:500;color:#222;letter-spacing:.2px}
.proj p{margin-top:10px;font-size:13.5px;line-height:26px;color:#777}
.proj a{display:inline-flex;align-items:center;gap:6px;margin-top:14px;font-size:15px;font-weight:500;color:var(--blue)}

/* contact */
.contact{top:3011px;left:0;width:1200px;height:483px}
.contact-bg{position:absolute;inset:0;background:
  radial-gradient(ellipse at 30% 40%,rgba(60,130,220,.6),transparent 60%),
  linear-gradient(135deg,#0b4aa2 0%,#0c3f8e 50%,#0a5bbf 100%)}
.contact .idx .num{color:#fff}
.contact .idx .dot{background:rgba(255,255,255,.45)}
.contact .idx .dot.on{background:var(--green)}
.contact .idx .dot span{color:#fff}
.more-info{position:absolute;left:119px;top:70px;color:#fff;font-size:17px}
.contact h2{position:absolute;left:119px;top:88px;color:#fff;font-size:35px;font-weight:500}
.info{position:absolute;left:121px;color:#fff;display:flex;align-items:center;gap:17px}
.info .ico{width:58px;height:58px;border-radius:50%;background:#fff;display:flex;align-items:center;justify-content:center}
.info .h{font-size:22px;line-height:30px}
.info .s{font-size:15px;line-height:26px}
.field{position:absolute;background:#fff;font-size:11px;color:#666;padding:12px 11px}
.send{position:absolute;left:420px;top:358px;width:453px;height:43px;background:var(--green-btn);color:#fff;font-size:14px;font-weight:500;display:flex;align-items:center;justify-content:center}
.map{position:absolute;left:889px;top:134px;width:208px;height:273px;background:linear-gradient(160deg,#f2f2f2,#e4e5e7)}
.map .pin{position:absolute;left:80px;top:90px}

/* footer */
.footer{top:3494px;left:0;width:1200px;height:254px;background:var(--footer);color:#fff}
.footer .brand{position:absolute;left:0;width:100%;justify-content:center;top:72px;font-size:24px;color:#fff}
.footer nav{position:absolute;top:150px;width:100%;display:flex;justify-content:center;gap:26px;font-size:16px;font-weight:500}
.footer .copy{position:absolute;top:196px;width:100%;text-align:center;font-size:13px}
</style>
</head>
<body>

<section class="abs hero">
  <div class="hero-bg" role="img" aria-label="City skyline at dusk with a dotted world map overlay"></div>
  <div class="brand"><span class="mark"></span>VEL-NORA GROUP</div>
  <nav class="nav">
    <a class="active" style="left:445px">Home</a>
    <a style="left:517px">About</a>
    <a style="left:590px">Services</a>
    <a style="left:677px">Projects</a>
    <a style="left:764px">Contact Us</a>
  </nav>
  <a class="btn-login">Log in</a>
  <a class="btn-register">Register</a>
  <div class="idx" style="top:247px">
    <div class="num">01</div>
    <div class="dots"><div class="dot on"><span>Landing</span></div><div class="dot"></div><div class="dot"></div><div class="dot"></div></div>
  </div>
  <h1>VEL - NORA GROUP</h1>
  <p class="lead">Lorem ipsum dolor sit amet, Sed consectetur adipiscing elit, sed</p>
  <svg class="scroll" width="22" height="32" viewBox="0 0 22 32"><rect x="1.5" y="1.5" width="19" height="29" rx="9.5" fill="none" stroke="#fff" stroke-width="2"/><line x1="11" y1="8" x2="11" y2="14" stroke="#fff" stroke-width="2"/></svg>
</section>

<section>
  <div class="ghost" style="left:-8px;top:686px;font-size:150px">ABOUT</div>
  <h2 class="abs about-title">DISCOVER OUR STORY</h2>
  <p class="abs about-sub">Lorem Ipsum sed amet</p>
  <div class="abs about-rule"></div>
  <p class="abs about-text">Lorem ipsum dolor sit amet, consectetur adipiscing elieiusmod tempor incididunt ut labore et dolore magna aliqua. kjendisse ultrices gravida. Risus commodo viverra maecenas accumsan lacus vel facilisis. Lorem ipsum dolor sit amet, consectetur adipiscing elieiusmod t incididunt ut labore et dolore magna aliqua.</p>
  <a class="abs learn"><span class="t">Learn More</span><span class="i"><svg width="10" height="16" viewBox="0 0 10 16"><path d="M2 2l6 6-6 6" fill="none" stroke="#0355a3" stroke-width="1.5"/></svg></span></a>
  <div class="idx" style="top:1089px">
    <div class="num">02</div>
    <div class="dots"><div class="dot on"><span>About</span></div><div class="dot"></div><div class="dot"></div><div class="dot"></div><div class="dot"></div><div class="dot"></div></div>
  </div>
  <div class="abs video" role="img" aria-label="Video cover: hand holding a young tree beside the company name"></div>
  <svg class="play" width="90" height="90" viewBox="0 0 90 90"><circle cx="45" cy="45" r="42" fill="#fff" stroke="#d9d9d9" stroke-width="4"/><path d="M36 28l26 17-26 17z" fill="#9a9a9a"/></svg>
</section>

<section>
  <div class="ghost" style="left:268px;top:1430px;font-size:128px">SERVICES</div>
  <h2 class="sec-title" style="top:1465px">WHAT WE DO</h2>
  <p class="sec-sub" style="top:1513px">Quis ipsum suspendisse ultrices gravida. Risus</p>
  <div class="idx" style="top:1680px">
    <div class="num">03</div>
    <div class="dots"><div class="dot"></div><div class="dot"></div><div class="dot on"><span>Services</span></div><div class="dot"></div><div class="dot"></div><div class="dot"></div></div>
  </div>

  <div class="card" style="left:112px">
    <div class="bg" role="img" aria-label="Glass towers seen from below" style="background:linear-gradient(160deg,#2a5d9b,#6f8db3 50%,#3b4d66)"></div><div class="shade"></div>
    <svg width="54" height="54" viewBox="0 0 54 54" fill="none" stroke="#fff" stroke-width="2"><circle cx="27" cy="27" r="24" stroke-dasharray="6 4"/><path d="M15 27l12-10 12 10v12H15z"/><rect x="23" y="30" width="8" height="9"/></svg>
    <h3>REAL ESTATE<br>DEVELOPMENT</h3><a class="more">Learn More</a>
  </div>
  <div class="card" style="left:359px">
    <div class="bg" role="img" aria-label="Team working on laptops" style="background:linear-gradient(160deg,#8a8a86,#5a5a56 60%,#2e2e2c)"></div><div class="shade"></div>
    <svg width="54" height="54" viewBox="0 0 54 54" fill="none" stroke="#fff" stroke-width="2"><circle cx="27" cy="13" r="6"/><circle cx="14" cy="20" r="5"/><circle cx="40" cy="20" r="5"/><path d="M10 42l10-8h14l10 8"/></svg>
    <h3 style="top:140px">MANAGEMENT</h3><a class="more">Learn More</a>
  </div>
  <div class="card" style="left:608px">
    <div class="bg" role="img" aria-label="Hands over financial papers" style="background:linear-gradient(160deg,#a79d8e,#c8c0b3 50%,#8a8275)"></div><div class="shade"></div>
    <svg width="54" height="54" viewBox="0 0 54 54" fill="none" stroke="#fff" stroke-width="2"><circle cx="27" cy="20" r="11"/><path d="M27 13v14M23 17h6a3 3 0 010 6h-4a3 3 0 000 6h6"/><path d="M8 42h14l10-4h14"/></svg>
    <h3 style="top:140px">FINANCING</h3><a class="more">Learn More</a>
  </div>
  <div class="card" style="left:855px">
    <div class="bg" role="img" aria-label="Laptop and charts on a desk" style="background:linear-gradient(160deg,#5f77a8,#a8b7d3 50%,#6b80aa)"></div><div class="shade"></div>
    <svg width="54" height="54" viewBox="0 0 54 54" fill="none" stroke="#fff" stroke-width="2"><path d="M27 30l-9-9a5 5 0 017-7l2 2 2-2a5 5 0 017 7z"/><path d="M8 40h12l8 4 16-8"/></svg>
    <h3 style="top:140px">MEDICAL</h3><a class="more">Learn More</a>
  </div>
</section>

<section>
  <div class="ghost" style="left:240px;top:1972px;font-size:128px">PARTNERS</div>
  <h2 class="sec-title" style="top:2007px">VEL - NORA GROUP PARTNERS</h2>
  <p class="sec-sub" style="top:2055px">Quis ipsum suspendisse ultrices gravida. Risus</p>
  <div class="idx" style="top:2120px">
    <div class="num">04</div>
    <div class="dots"><div class="dot"></div><div class="dot"></div><div class="dot"></div><div class="dot on"><span>Partners</span></div><div class="dot"></div><div class="dot"></div></div>
  </div>
  <div class="partner sel" style="left:112px"><div class="badge" role="img" aria-label="382 Builders badge"></div></div>
  <div class="partner" style="left:359px"><div class="badge" role="img" aria-label="Pordiva badge"></div></div>
  <div class="partner" style="left:606px"><div class="badge" role="img" aria-label="Soundpoise badge"></div></div>
  <div class="partner dark" style="left:853px"><div class="badge" role="img" aria-label="QRT Dental Services badge" style="background:#2b3a55"></div></div>
  <svg class="pointer" width="16" height="11" viewBox="0 0 16 11"><path d="M0 0h16L8 11z" fill="#8cc63f"/></svg>
  <h3 class="abs partner-head">OUR CONSTRUCTION PARTNER:</h3>
  <p class="abs partner-text">Lorem ipsum dolor sit amet, consectetur adipiscing elit, sed do eiusmod tempor incididunt ut labore et dolore magna aliqua. Quis ipsum suspendisse ultrices gravida. Risus commodo viverra maecenas accumsan lacus vel facilisis.</p>
</section>

<section>
  <div class="ghost" style="left:250px;top:2420px;font-size:128px">PROJECTS</div>
  <h2 class="sec-title" style="top:2454px">PROPOSED PROJECTS</h2>
  <p class="sec-sub" style="top:2502px">Quis ipsum suspendisse ultrices gravida. Risus</p>
  <div class="idx" style="top:2670px">
    <div class="num">05</div>
    <div class="dots"><div class="dot"></div><div class="dot"></div><div class="dot"></div><div class="dot"></div><div class="dot on"><span>Projects</span></div><div class="dot"></div></div>
  </div>
  <div class="proj-img" role="img" aria-label="Site plan drawing of Hollowmere Business Park" style="left:112px;width:313px;background:linear-gradient(180deg,#f3f3f3,#dcdcdc)"></div>
  <div class="proj-img" role="img" aria-label="Rendering of Cresfield Business Park building" style="left:444px;width:312px;background:linear-gradient(180deg,#bdbdbd,#555 60%,#2c2c2c)"></div>
  <div class="proj-img" role="img" aria-label="Aerial view of the Mt. Corwin Ridge Professional location" style="left:775px;width:313px;background:linear-gradient(160deg,#6c6c6c,#a0a0a0 50%,#3e3e3e)"></div>
  <div class="proj" style="left:112px"><h4>HOLLOWMERE BUSINESS PARK</h4><p>Lorem ipsum dolor sit amet, consectetur adipiscing elit, sed do eiusmod tempor incididunt ut labore et dolore magna</p><a>Learn More <svg width="16" height="8" viewBox="0 0 16 8"><path d="M0 4h14M10 1l4 3-4 3" fill="none" stroke="#0355a3" stroke-width="1.6"/></svg></a></div>
  <div class="proj" style="left:444px"><h4>CRESFIELD BUSINESS PARK</h4><p>Lorem ipsum dolor sit amet, consectetur adipiscing elit, sed do eiusmod tempor incididunt ut labore et dolore magna</p><a>Learn More <svg width="16" height="8" viewBox="0 0 16 8"><path d="M0 4h14M10 1l4 3-4 3" fill="none" stroke="#0355a3" stroke-width="1.6"/></svg></a></div>
  <div class="proj" style="left:775px"><h4>MT. CORWIN RIDGE PROFESSIONAL</h4><p>Lorem ipsum dolor sit amet, consectetur adipiscing elit, sed do eiusmod tempor incididunt ut labore et dolore magna</p><a>Learn More <svg width="16" height="8" viewBox="0 0 16 8"><path d="M0 4h14M10 1l4 3-4 3" fill="none" stroke="#0355a3" stroke-width="1.6"/></svg></a></div>
</section>

<section class="abs contact">
  <div class="contact-bg" role="img" aria-label="Blue world map pattern with financial figures"></div>
  <div class="idx" style="top:132px">
    <div class="num">06</div>
    <div class="dots"><div class="dot"></div><div class="dot"></div><div class="dot"></div><div class="dot"></div><div class="dot"></div><div class="dot on"><span>contact</span></div></div>
  </div>
  <p class="more-info">MORE INFO</p>
  <h2>CONTACT US</h2>
  <div class="info" style="top:150px"><div class="ico"><svg width="26" height="30" viewBox="0 0 26 30" fill="none" stroke="#0355a3" stroke-width="1.6"><path d="M13 28S3 17 3 11a10 10 0 0120 0c0 6-10 17-10 17z"/><circle cx="13" cy="11" r="4"/></svg></div><div><div class="h">Address</div><div class="s">1234 sed Location<br>000 Ny 0000</div></div></div>
  <div class="info" style="top:263px"><div class="ico"><svg width="24" height="30" viewBox="0 0 24 30" fill="none" stroke="#0355a3" stroke-width="1.6"><rect x="6" y="3" width="12" height="24" rx="2"/><line x1="10" y1="23" x2="14" y2="23"/></svg></div><div><div class="h">Give Usa Call</div><div class="s">(888) 888 8888</div></div></div>
  <div class="info" style="top:342px"><div class="ico"><svg width="28" height="22" viewBox="0 0 28 22" fill="none" stroke="#0355a3" stroke-width="1.6"><rect x="2" y="2" width="24" height="18" rx="2"/><path d="M2 3l12 9 12-9"/></svg></div><div><div class="h">Send Us a Message</div><div class="s">info@velnoragroup.com</div></div></div>
  <div class="field" style="left:420px;top:138px;width:227px;height:46px">Name*</div>
  <div class="field" style="left:662px;top:138px;width:211px;height:46px">Email*</div>
  <div class="field" style="left:420px;top:193px;width:453px;height:47px">Subject</div>
  <div class="field" style="left:420px;top:252px;width:453px;height:96px">Message*</div>
  <a class="send">Send Message</a>
  <div class="map" role="img" aria-label="Street map around the office location">
    <svg class="pin" width="48" height="48" viewBox="0 0 48 48"><circle cx="24" cy="24" r="23" fill="#0355a3"/><path d="M24 35s-7-8-7-13a7 7 0 0114 0c0 5-7 13-7 13z" fill="none" stroke="#fff" stroke-width="1.6"/><circle cx="24" cy="22" r="2.5" fill="none" stroke="#fff" stroke-width="1.6"/></svg>
  </div>
</section>

<footer class="abs footer">
  <div class="brand"><span class="mark"></span>VEL-NORA GROUP</div>
  <nav><a>Home</a><a>About</a><a>Services</a><a>Projects</a><a>Contact Us</a></nav>
  <p class="copy">Copyright © 2020. All Rights Reserved</p>
</footer>

</body>
</html>
```